Home page design for Drone video business (the Business focusses on home videos for realtors)

Dear reader,

*I NEED DESIGNS OF ALL THE PAGES*
We need a first design of a homepage and of 4 other pages of the website of a business that sells drone video services. All the pages will need to be in the similar design style.
The video's are targeted at consumers that want to sell there home and would like to have a cool drone video of photos of their home.

How does the website look:
- has a navbar on top
- A cool looking banner of an areal drone.
- A Big header: with company name: SkyNestReels
- A smaller subheader: We film your home to increase your chances of sale
- Then a section with a Big header: How does it work
- In this section a place for a vimeo explainitory video
- Then a similar navbar styled bar with a phone number and a email address
- Then a section where the videos porfolio is displayed in a cool way
- Inside this sectiona header: Our work

- A section with header: Why us?
- 4 symbols here with a subheader and some lorum ipsum text underneath (see wireframe images)

- Under that a: Contact us
- where you can put in name, email, phone, message box and a send button

- At the bottom a footer with phone number and a fake address for now.

Be creative. Use creative but serious color.
Use a serious font. Make it a sharp design. Sharp lines. Not to dark design and not to light design.

The wireframes are the same kind of images.
PLEASE PUT IN DESIGNS OF ALL THE PAGES

Good luck

Target Market(s)

People that want to sell home and want to make a cool drone video or photos of their home.

Industry/Entity Type

Business

Contact Information for Business Card

Milo Brenning
milo@skynestreels.example
+31647283915

Logo Text

SkyNestReels

Number of Pages Required

1 page

Font styles to use
Sans Serif

Requirements
Must have
• All the sections as explained in the instructions.
• The nav bar should have an about us, services, portfolio and a contact us buttons.
• See instruction for details.
• Must include designs of the front page, contact us, our services, portfolio and contact us.
• If you do add some designs for the "about us", "services", "prices", "portfolio" and "contact us" pages, you make a way better chance of winning the competition.
Nice to have
• designs for the other pages as described at the Must haves. You make a better chance of winning if you include them. Look at the wireframes to see the mockups for those pages. think creative about what kind of sections and design should be included in those pages.
Should not have
• bad designs.

```html
<!DOCTYPE html>
<html lang="en">
<head>
<meta charset="utf-8">
<title>SkyNestReels – Home</title>
<link rel="stylesheet" href="https://fonts.googleapis.com/css2?family=Exo+2:wght@600;700&family=Lato:wght@400;700&display=swap">
<style>
:root{
  --red:#a3171c;
  --ink:#222222;
  --muted:#555555;
  --light:#f2f2f2;
  --line:#d6d6d6;
  --white:#ffffff;
  --footer:#1f1f1f;
  --night1:#2b3a4c;
  --night2:#4d6277;
}
*{box-sizing:border-box;margin:0;padding:0}
html,body{width:1200px;height:2446px;overflow:hidden}
body{font-family:"Lato",Arial,sans-serif;color:var(--ink);background:var(--white);position:relative}
.abs{position:absolute}
.heading{font-family:"Exo 2",Arial,sans-serif;font-weight:700;font-size:36px;letter-spacing:1px;text-align:center;width:100%;left:0}
.heading em{font-style:normal;color:var(--red)}
.rule{height:1px;background:var(--line);left:50%;transform:translateX(-50%)}

/* nav */
.navbar{top:0;left:0;width:1200px;height:65px;background:var(--white);border-bottom:1px solid var(--line)}
.brand{left:101px;top:16px;display:flex;align-items:center;gap:10px;font-family:"Lato",sans-serif;font-weight:700;font-size:26px;color:var(--ink)}
.brand-dot{width:22px;height:22px;background:var(--red)}
.menu{right:92px;top:19px;display:flex;align-items:center;font-family:"Lato",sans-serif;font-weight:700;font-size:15px}
.menu a{color:var(--ink);text-decoration:none;padding:6px 26px;border-left:1px solid var(--line)}
.menu a:first-child{border-left:none}
.menu a.active{color:var(--red);border:2px solid var(--red);padding:6px 20px;margin-right:0}
.menu a.active + a{border-left:none}

/* hero */
.hero{top:65px;left:0;width:1200px;height:497px;background:linear-gradient(180deg,#8f9aa6 0%,#b4bcc4 45%,#6f7a6a 72%,#4f5a4c 100%)}
.hero-title{top:370px;width:100%;text-align:center;color:var(--white);font-family:"Exo 2",sans-serif;font-weight:700;font-size:44px;text-shadow:0 2px 4px rgba(0,0,0,.45)}
.hero-sub{top:432px;width:100%;text-align:center;color:var(--white);font-family:"Exo 2",sans-serif;font-weight:600;font-size:30px;line-height:40px;text-shadow:0 2px 4px rgba(0,0,0,.45)}
.dots{top:532px;left:570px;display:flex;gap:6px}
.dots span{width:10px;height:10px;border-radius:50%;background:rgba(255,255,255,.7)}
.dots span:first-child{background:var(--white)}

/* how it works */
.how{top:562px;left:0;width:1200px;height:568px;background:var(--light)}
.screen{left:196px;top:750px;width:458px;height:260px;background:linear-gradient(160deg,#9fc3dc 0%,#6f8fa8 45%,#5c6c70 100%)}
.play{left:384px;top:855px;width:50px;height:50px;border-radius:50%;background:rgba(255,255,255,.85)}
.contact-line{left:710px;display:flex;align-items:center;gap:18px;font-size:29px;color:var(--ink)}
.ring{width:72px;height:72px;border-radius:50%;border:2px solid var(--red);display:flex;align-items:center;justify-content:center}

/* work */
.card{top:1286px;width:292px;height:251px;background:var(--white);border:1px solid var(--line);padding:9px}
.card .photo{width:100%;height:100%;position:relative}
.card .yt{position:absolute;left:50%;top:50%;width:50px;height:34px;margin:-17px 0 0 -25px;border-radius:8px;background:#c4191f}
.card .yt:after{content:"";position:absolute;left:20px;top:10px;border-left:13px solid #fff;border-top:7px solid transparent;border-bottom:7px solid transparent}

/* why */
.why{top:1597px;left:0;width:1200px;height:395px;background:linear-gradient(180deg,var(--night1) 0%,var(--night2) 60%,#3d4e5f 100%)}
.feature{top:1718px;width:240px;text-align:center;color:var(--white)}
.feature .icon{width:110px;height:110px;border-radius:50%;border:3px solid var(--white);margin:0 auto;display:flex;align-items:center;justify-content:center}
.feature .icon.on{background:var(--red)}
.feature h3{font-family:"Exo 2",sans-serif;font-weight:700;font-size:17px;margin-top:24px}
.feature p{font-size:13px;line-height:21px;margin-top:12px}

/* contact */
.contact{top:1992px;left:0;width:1200px;height:404px;background:linear-gradient(135deg,#eef0ee 0%,#f4f2ea 50%,#e9eef2 100%)}
.field{border:1px solid #bdbdbd;background:rgba(255,255,255,.75);font-size:13px;color:var(--ink);padding:12px 10px}
.submit{left:536px;top:2303px;width:127px;height:43px;background:var(--red);color:var(--white);font-family:"Lato",sans-serif;font-weight:700;font-size:16px;display:flex;align-items:center;justify-content:center;border:none}

/* footer */
.footer{top:2396px;left:0;width:1200px;height:50px;background:var(--footer);color:var(--white);font-size:15px}
.foot-item{top:14px;display:flex;align-items:center;gap:10px}
.copyright{right:96px;top:17px;font-size:12px;font-weight:700}
</style>
</head>
<body>

<header class="navbar abs">
  <div class="brand abs"><span class="brand-dot"></span>SkyNestReels</div>
  <nav class="menu abs">
    <a class="active" href="#">HOME</a>
    <a href="#">SERVICES</a>
    <a href="#">ABOUT US</a>
    <a href="#">PORTFOLIO</a>
    <a href="#">CONTACT US</a>
  </nav>
</header>

<section class="hero abs" role="img" aria-label="Aerial drone hovering over a blurred landscape"></section>
<h1 class="hero-title abs">SKYNESTREELS</h1>
<p class="hero-sub abs">WE FILM YOUR HOME TO<br>INCREASE YOUR CHANCES OF SALE</p>
<div class="dots abs"><span></span><span></span><span></span><span></span></div>

<section class="how abs"></section>
<h2 class="heading abs" style="top:609px">HOW DOES IT <em>WORK?</em></h2>
<div class="rule abs" style="top:668px;width:400px"></div>
<svg class="abs" style="left:173px;top:725px" width="503" height="400" viewBox="0 0 503 400">
  <rect x="0" y="0" width="503" height="314" rx="14" fill="#111"/>
  <path d="M210 314 L295 314 L300 362 Q340 385 345 400 L158 400 Q165 385 205 362 Z" fill="#111"/>
</svg>
<div class="screen abs" role="img" aria-label="Explainer video still of a drone over a city skyline"></div>
<svg class="abs" style="left:384px;top:855px" width="50" height="50" viewBox="0 0 50 50">
  <circle cx="25" cy="25" r="25" fill="rgba(255,255,255,.85)"/>
  <path d="M20 15 L35 25 L20 35 Z" fill="#a3171c"/>
</svg>
<div class="contact-line abs" style="top:800px">
  <span class="ring"><svg width="32" height="32" viewBox="0 0 24 24"><path d="M6.6 10.8a15 15 0 0 0 6.6 6.6l2.2-2.2a1 1 0 0 1 1-.25 11.4 11.4 0 0 0 3.6.57 1 1 0 0 1 1 1V20a1 1 0 0 1-1 1A17 17 0 0 1 3 4a1 1 0 0 1 1-1h3.5a1 1 0 0 1 1 1c0 1.25.2 2.45.57 3.6a1 1 0 0 1-.25 1z" fill="#a3171c"/></svg></span>
  +31647283915
</div>
<div class="contact-line abs" style="top:902px">
  <span class="ring"><svg width="34" height="24" viewBox="0 0 34 24"><rect width="34" height="24" fill="#a3171c"/><path d="M1 1 L17 13 L33 1 M1 23 L13 11 M33 23 L21 11" stroke="#fff" stroke-width="2" fill="none"/></svg></span>
  contact@skynestreels.example
</div>

<h2 class="heading abs" style="top:1187px">OUR <em>WORK?</em></h2>
<div class="rule abs" style="top:1246px;width:270px"></div>
<svg class="abs" style="left:42px;top:1382px" width="32" height="58" viewBox="0 0 32 58"><path d="M30 2 L3 29 L30 56" stroke="#bbb" stroke-width="2" fill="none"/></svg>
<svg class="abs" style="left:1126px;top:1382px" width="32" height="58" viewBox="0 0 32 58"><path d="M2 2 L29 29 L2 56" stroke="#bbb" stroke-width="2" fill="none"/></svg>
<div class="card abs" style="left:99px"><div class="photo" role="img" aria-label="Drone pilot filming a house" style="background:linear-gradient(180deg,#3f86c8 0%,#8fbde0 55%,#c9b58a 100%)"><span class="yt"></span></div></div>
<div class="card abs" style="left:453px"><div class="photo" role="img" aria-label="Drone above a two-storey home" style="background:linear-gradient(180deg,#cfd3d6 0%,#a99b86 55%,#6e7058 100%)"><span class="yt"></span></div></div>
<div class="card abs" style="left:807px"><div class="photo" role="img" aria-label="Drone over a house in winter" style="background:linear-gradient(180deg,#a9c4e3 0%,#7b6f62 55%,#e6e8ec 100%)"><span class="yt"></span></div></div>

<section class="why abs" role="img" aria-label="Drone flying over a coastal city skyline"></section>
<h2 class="heading abs" style="top:1623px;color:var(--white)">WHY US?</h2>
<div class="rule abs" style="top:1684px;width:300px;background:rgba(255,255,255,.5)"></div>
<div class="feature abs" style="left:76px">
  <div class="icon on"><svg width="56" height="56" viewBox="0 0 56 56" fill="none" stroke="#fff" stroke-width="4"><circle cx="12" cy="12" r="7"/><circle cx="44" cy="12" r="7"/><circle cx="12" cy="44" r="7"/><circle cx="44" cy="44" r="7"/><path d="M17 17 L39 39 M39 17 L17 39"/></svg></div>
  <h3>CHEAP</h3>
  <p>Lorem ipsum dolor sit amet,<br>consectetuer sit al adipiscing elit,<br>sed diam nonummy.</p>
</div>
<div class="feature abs" style="left:330px">
  <div class="icon"><svg width="56" height="56" viewBox="0 0 56 56" fill="none" stroke="#fff" stroke-width="3"><circle cx="14" cy="14" r="9"/><circle cx="42" cy="14" r="9"/><circle cx="14" cy="42" r="9"/><circle cx="42" cy="42" r="9"/><rect x="22" y="22" width="12" height="12" fill="#fff"/></svg></div>
  <h3>FLEXIBLE</h3>
  <p>Lorem ipsum dolor sit amet,<br>consectetuer sit al adipiscing elit,<br>sed diam nonummy.</p>
</div>
<div class="feature abs" style="left:583px">
  <div class="icon"><svg width="56" height="44" viewBox="0 0 56 44"><rect x="4" y="4" width="48" height="30" fill="none" stroke="#fff" stroke-width="3"/><text x="28" y="26" text-anchor="middle" font-family="Lato,sans-serif" font-weight="700" font-size="16" fill="#fff">4K</text><path d="M20 40 H36" stroke="#fff" stroke-width="3"/></svg></div>
  <h3>4K QUALITY</h3>
  <p>Lorem ipsum dolor sit amet,<br>consectetuer sit al adipiscing elit,<br>sed diam nonummy.</p>
</div>
<div class="feature abs" style="left:851px">
  <div class="icon"><svg width="60" height="48" viewBox="0 0 60 48" fill="none" stroke="#fff" stroke-width="3"><path d="M6 14 H54 M18 14 V22 H42 V14 M22 22 L14 40 M38 22 L46 40"/><circle cx="30" cy="8" r="4" fill="#a3171c" stroke="none"/></svg></div>
  <h3>INCREASE SALE CHANCE</h3>
  <p>Lorem ipsum dolor sit amet,<br>consectetuer sit al adipiscing elit,<br>sed diam nonummy.</p>
</div>

<section class="contact abs" role="img" aria-label="Street map of the office surroundings"></section>
<h2 class="heading abs" style="top:2034px">CONTACT <em>US</em></h2>
<div class="field abs" style="left:124px;top:2117px;width:300px;height:43px">Name</div>
<div class="field abs" style="left:450px;top:2117px;width:298px;height:43px">Email</div>
<div class="field abs" style="left:776px;top:2117px;width:300px;height:43px">Phone</div>
<div class="field abs" style="left:124px;top:2183px;width:952px;height:92px">Message</div>
<button class="submit abs">SUBMIT</button>

<footer class="footer abs">
  <div class="foot-item abs" style="left:98px">
    <svg width="18" height="22" viewBox="0 0 24 24"><path d="M6.6 10.8a15 15 0 0 0 6.6 6.6l2.2-2.2a1 1 0 0 1 1-.25 11.4 11.4 0 0 0 3.6.57 1 1 0 0 1 1 1V20a1 1 0 0 1-1 1A17 17 0 0 1 3 4a1 1 0 0 1 1-1h3.5a1 1 0 0 1 1 1c0 1.25.2 2.45.57 3.6a1 1 0 0 1-.25 1z" fill="#fff"/></svg>
    +31647283915
  </div>
  <div class="foot-item abs" style="left:262px">
    <svg width="24" height="17" viewBox="0 0 34 24"><rect width="34" height="24" fill="#fff"/><path d="M1 1 L17 13 L33 1" stroke="#1f1f1f" stroke-width="2" fill="none"/></svg>
    contact@skynestreels.example
  </div>
  <div class="copyright abs">COPYRIGHT © 2016 SKYNESTREELS. ALL RIGHTS RESERVED.</div>
</footer>

</body>
</html>
```